Web design for Frostwerkly.com

We need a website (4 starter pages) designed for a drupal based site. The theme is flexible so I am open to different designs/looks. I am looking for a VERY simple and clean and FUN design to make it easy to use for the customer.

Our company is similar to Pitch lantern as in it's for multiple people to design a cake for a customer and they choose a winning design and work with that cake designer to make the cake (birthday, wedding etc...)

Our vision:
First page:
2 main images for either the customer to submit an idea for a cake, or the new designer to sign up to the site. Perhaps a mouse-over with wording on what the options are? You can use this site:
http://www.plumwidget.example/ as a sort of template but more clean and simple

"How it works" page:
Similar to this:
http://www.plumwidget.example/how-it-works
Fun, clean and simple

Submit cake design page (form submission)

Submit new designer page

Ideally a 960 wide design with no flash, but open to a flash design if it stands out...

Please contact me if you have any questions!

Target Market(s)

People who want a custom cake made, and people who design and make cakes.

Industry/Entity Type

Wedding

Requirements
Must have
• Use the logo attached. The "Tater Bop" should be a big part of the site...kind of a site mascot?
Nice to have
• 960 wide
No flash but not a deal-breaker if there is flash and it's amazing...

```html
<!DOCTYPE html>
<html lang="en">
<head>
<meta charset="utf-8">
<title>Frostwerkly.com</title>
<link href="https://fonts.googleapis.com/css2?family=Source+Sans+3:ital,wght@0,400;0,600;0,700;1,400&display=swap" rel="stylesheet">
<style>
:root{
  --cream:#f3ebe5;
  --cream-deep:#ece2da;
  --brown:#5c4336;
  --brown-dark:#4a3327;
  --ink:#4a2c1f;
  --title:#3b2418;
  --white:#ffffff;
  --frame:#5a3d30;
}
*{margin:0;padding:0;box-sizing:border-box}
html,body{width:994px;height:1200px;overflow:hidden;background:var(--cream)}
body{font-family:"Source Sans 3",Arial,sans-serif;color:var(--ink)}
.page{position:absolute;left:0;top:0;width:960px;height:1160px;transform:scale(1.0354,1.0345);transform-origin:0 0;background:var(--cream)}
.abs{position:absolute}
.header-band{left:0;top:10px;width:960px;height:382px;background:var(--brown)}
.content-panel{left:12px;top:128px;width:932px;height:979px;background:var(--white)}
.logo{left:27px;top:56px;display:flex;align-items:center;gap:8px;font-size:30px;font-weight:700;color:var(--white);letter-spacing:-.5px}
.logo-dot{width:14px;height:14px;border-radius:50%;background:#e9a9bf}
.search{left:725px;top:45px;width:188px;height:20px;border-radius:10px;background:var(--white);font-size:11px;color:#6b5a52;padding:3px 0 0 11px}
.search svg{position:absolute;right:7px;top:3px}
.nav{left:327px;top:91px;width:615px;height:37px;background:var(--brown-dark);border-radius:10px 10px 0 0;display:flex;padding-left:10px}
.nav a{color:var(--white);text-decoration:none;font-size:14px;line-height:37px;padding:0 24px;border-right:1px solid #7a5e50}
.nav a:last-child{border-right:0}
.slider{left:24px;top:140px;width:908px;height:310px;border:3px solid var(--frame);border-radius:3px;background:var(--white);box-shadow:0 12px 10px -8px rgba(0,0,0,.35)}
.slider-photo{left:0;top:0;width:609px;height:304px;background:radial-gradient(ellipse at 55% 45%,#8a4a30 0%,#5e3020 45%,#c9bdb8 72%,#eeeae8 100%)}
.slider-arrow{left:10px;top:112px}
.slider-copy{left:610px;top:0;width:292px;height:304px;background:linear-gradient(135deg,#fff 60%,#f2ece7);border-left:1px solid #c9b8ae}
.slider-copy h1{position:absolute;left:18px;top:22px;font-size:26px;font-weight:400;color:#4a3a33}
.slider-copy p{position:absolute;left:21px;top:58px;width:256px;font-size:11.3px;line-height:17px;color:#5a4337}
.cta{left:610px;width:299px;height:32px;background:linear-gradient(90deg,#faf6f3,#e8ddd4);font-size:17px;color:#5a4337;padding:5px 0 0 25px}
.cta::before{content:"";position:absolute;left:24px;top:12px;width:6px;height:6px;border-right:2px solid #3b2418;border-top:2px solid #3b2418;transform:rotate(45deg)}
.cta span{margin-left:20px}
.section-title{font-size:20px;font-weight:400;color:var(--title)}
.rule{height:1px;background:linear-gradient(90deg,#5c4336 70%,rgba(92,67,54,0))}
.body-text{font-size:11.6px;line-height:17px;color:var(--ink)}
.pill{width:106px;height:19px;border-radius:10px;background:var(--cream-deep);font-size:11px;color:#5a4337;text-align:center;line-height:19px}
.thumb{border:3px solid var(--frame)}
.sidebar{left:618px;top:472px;width:326px;height:635px;background:linear-gradient(180deg,#f5efeb,#fbf8f6 60%,#f5efeb)}
.post-thumb{width:82px;height:76px;border:1px solid #8a7266}
.post-title{font-size:12.5px;font-weight:700;color:var(--title)}
.post-text{font-size:11.5px;line-height:17px;width:190px}
.post-meta{font-size:11px}
.dots{height:0;border-top:2px dotted #5c4336;width:284px}
.testimonial{left:636px;top:923px;width:294px;height:163px;border:1px solid #c9b5a8;border-radius:12px;background:var(--cream-deep)}
.testimonial p{position:absolute;left:16px;top:12px;width:262px;font-size:11.3px;line-height:19px;font-style:italic}
.testimonial cite{position:absolute;right:18px;top:133px;font-size:13px;font-style:italic}
.footer{left:0;top:1107px;width:960px;height:53px;background:var(--brown);color:var(--white);font-size:11px}
</style>
</head>
<body>
<div class="page">
  <div class="abs header-band"></div>
  <div class="abs content-panel"></div>

  <div class="abs logo"><span class="logo-dot"></span>Frostwerkly.com</div>
  <div class="abs search">type your word here
    <svg width="16" height="14" viewBox="0 0 16 14"><circle cx="6" cy="6" r="4.5" fill="none" stroke="#8a8a8a" stroke-width="1.6"/><line x1="9.5" y1="9" x2="14.5" y2="13" stroke="#8a8a8a" stroke-width="2"/></svg>
  </div>
  <nav class="abs nav"><a>HOME</a><a>ABOUT US</a><a>SERVICES</a><a>PRODUCTS</a><a>SUBMIT</a><a>CONTACT US</a></nav>

  <div class="abs slider">
    <div class="abs slider-photo" role="img" aria-label="Chocolate cake topped with chocolate shards and strawberries"></div>
    <svg class="abs slider-arrow" width="24" height="80" viewBox="0 0 24 80"><polyline points="20,2 2,40 20,78" fill="none" stroke="#222" stroke-width="1.5"/></svg>
    <div class="abs slider-copy">
      <h1>Frostwerkly here..</h1>
      <p>We ensure that our designs represent the client area to perfection and look convincing to the targeted audience as well. We believe that you need us to represent beautifully the unique way of your doing the business. We design user-friendly website that forces the viewer to return to the website again and again. The company has some of the finest talents in industry.</p>
    </div>
    <div class="abs cta" style="top:220px"><span>Submit an idea for a cake</span></div>
    <div class="abs cta" style="top:258px"><span>New designer ? sign up</span></div>
  </div>

  <h2 class="abs section-title" style="left:32px;top:488px">Welcome to Our Company Website</h2>
  <div class="abs rule" style="left:32px;top:517px;width:560px"></div>
  <p class="abs body-text" style="left:33px;top:525px;width:560px">We have learnt that designing is not only inclined to powerful imaginations but also focused and attractive to expected viewers also. At Brightforge esolutions we use all the latest technologies for web designing.</p>
  <p class="abs body-text" style="left:33px;top:566px;width:562px">Brightforge esolutions provides the best web designing which compels the customers to ask and inquire about. We ensure that our designs represent the client area to perfection and look convincing to the targeted audience as well. We believe that you need us to represent beautifully the unique way of your doing the business. We design user-friendly website that forces the viewer to return to the website again and again. The company has some of the finest talents in industry.</p>
  <div class="abs pill" style="left:28px;top:661px">READ MORE</div>

  <h2 class="abs section-title" style="left:33px;top:723px">Our Best Cakes</h2>
  <div class="abs rule" style="left:32px;top:751px;width:556px"></div>
  <div class="abs thumb" style="left:30px;top:763px;width:178px;height:115px;background:linear-gradient(160deg,#e9eef5,#f6e3e3 50%,#d9475a)" role="img" aria-label="Heart-shaped cream cake with raspberries"></div>
  <div class="abs thumb" style="left:218px;top:763px;width:179px;height:115px;background:linear-gradient(160deg,#f3ece3,#f3ec9a 55%,#e6dcc4)" role="img" aria-label="Slice of cheesecake with strawberry and cream"></div>
  <div class="abs thumb" style="left:406px;top:763px;width:178px;height:115px;background:linear-gradient(160deg,#7a2c1e,#d8b8a0 50%,#3a2a22)" role="img" aria-label="Ruffled cake decorated with flowers"></div>
  <div class="abs thumb" style="left:31px;top:887px;width:179px;height:116px;background:linear-gradient(160deg,#c84a30,#f0ece6 45%,#3a2418)" role="img" aria-label="Striped chocolate and cream cake with berries"></div>
  <div class="abs thumb" style="left:220px;top:887px;width:179px;height:116px;background:linear-gradient(160deg,#d9cfc6,#4a2a1c 50%,#2e1a12)" role="img" aria-label="Chocolate cake with piped frosting"></div>
  <div class="abs thumb" style="left:408px;top:887px;width:178px;height:116px;background:linear-gradient(160deg,#f2eee8,#3a1a10 50%,#c0303a)" role="img" aria-label="Chocolate mousse cake with gold leaf and raspberries"></div>
  <div class="abs pill" style="left:30px;top:1026px">VIEW ALL</div>

  <aside class="abs sidebar"></aside>
  <h2 class="abs section-title" style="left:637px;top:492px;font-size:19px">Recent Blog &amp; Comments</h2>
  <div class="abs rule" style="left:637px;top:528px;width:286px;background:#5c4336"></div>

  <div class="abs post-thumb" style="left:636px;top:542px;background:linear-gradient(160deg,#5d7a9a,#8a6ab8 45%,#ece8ee)" role="img" aria-label="Cake with purple flower decoration"></div>
  <div class="abs post-title" style="left:728px;top:540px">CAKE NAME GOES HERE</div>
  <p class="abs post-text" style="left:727px;top:563px">We design user-friendly website that forces the viewer to return</p>
  <div class="abs post-meta" style="left:728px;top:601px">POSTED &nbsp; 01 FEB 2012 &nbsp;&nbsp; | &nbsp;&nbsp;Read More</div>
  <div class="abs dots" style="left:637px;top:630px"></div>

  <div class="abs post-thumb" style="left:636px;top:652px;background:linear-gradient(160deg,#f4f0ec,#4a2a1c 50%,#e8e2dc)" role="img" aria-label="Slice of chocolate layer cake"></div>
  <div class="abs post-title" style="left:728px;top:650px">CAKE NAME GOES HERE</div>
  <p class="abs post-text" style="left:727px;top:673px">We design user-friendly website that forces the viewer to return to the</p>
  <div class="abs post-meta" style="left:728px;top:714px">POSTED &nbsp; 01 FEB 2012 &nbsp;&nbsp; | &nbsp;&nbsp;Read More</div>
  <div class="abs dots" style="left:637px;top:744px"></div>

  <div class="abs post-thumb" style="left:636px;top:763px;background:linear-gradient(160deg,#3a6a9a,#eef2f6 50%,#7aa8d8)" role="img" aria-label="White cake with blue flower decorations"></div>
  <div class="abs post-title" style="left:728px;top:761px">CAKE NAME GOES HERE</div>
  <p class="abs post-text" style="left:727px;top:784px">We design user-friendly website that forces the viewer to return to the</p>
  <div class="abs post-meta" style="left:728px;top:825px">POSTED &nbsp; 01 FEB 2012 &nbsp;&nbsp; | &nbsp;&nbsp;Read More</div>

  <h2 class="abs section-title" style="left:640px;top:891px">Testimonials</h2>
  <div class="abs testimonial">
    <p>When considering advanced web development project, finding the right answers to the hard questions is a challenge for any firm, it includes expertise and enables Brightforge eSolutions to specialize in advanced projects and ongoing projects that require permanent support and maintenance.</p>
    <cite>by Author Name..</cite>
  </div>

  <footer class="abs footer">
    <div class="abs" style="left:33px;top:12px">Copyright © 2012 Company Name &nbsp; | &nbsp; All right reserved</div>
    <div class="abs" style="left:662px;top:12px">Home &nbsp;|&nbsp; About Us &nbsp;|&nbsp; Cakes &nbsp;|&nbsp; Recent Posts &nbsp;|&nbsp; Contact Us</div>
  </footer>
</div>
</body>
</html>
```